Lawnmowing and maintenance business card and letterhead design

We need a business card design and a letter head design for a new company we are starting up.

I would like to include pictures of a cartoon ride on mower with a few tools on board, a cartoon person vacuuming staircase and a cartoon person dusting.

Our business will be handling looking after unit public areas, ie garden maintenance - mowing, trimming trees, blowing leaves.
Also dusting, vacuuming, window cleaning.

Industry/Entity Type

Business

Contact Information for Business Card

Tolvane lawnmowing and property maintenance
14 Barlowe Crescent
Wexley Heights NSW 2184
0491726048
0478301652

Requirements
Must have
• Must have the business name, business address, abn number 64 907 518 243, business phone numbers pictures as above

```html
<!DOCTYPE html>
<html lang="en">
<head>
<meta charset="utf-8">
<title>Tolvane – Stationery Set</title>
<link rel="stylesheet" href="https://fonts.googleapis.com/css2?family=Fira+Sans:wght@300;400&display=swap">
<style>
  :root {
    --backdrop: #5a6766;
    --paper: #ffffff;
    --brand-red: #e8262a;
    --ink: #1e1e1e;
    --mascot-top: #8a5a3c;
    --mascot-mid: #6d8fd6;
    --mascot-low: #7a5fb0;
  }
  * { box-sizing: border-box; margin: 0; padding: 0; }
  html, body {
    width: 1200px; height: 794px; overflow: hidden;
    background: var(--backdrop);
    font-family: "Fira Sans", Arial, sans-serif;
    font-weight: 300;
  }
  .canvas { position: relative; width: 1200px; height: 794px; }
  .sheet { position: absolute; background: var(--paper); overflow: hidden; }
  .card-front { left: 33px; top: 35px; width: 520px; height: 320px; }
  .card-back  { left: 33px; top: 444px; width: 520px; height: 320px; }
  .letterhead { left: 613px; top: 11px; width: 549px; height: 753px; }

  .mascot {
    position: absolute;
    background: linear-gradient(180deg, var(--mascot-top) 0%, var(--mascot-mid) 50%, var(--mascot-low) 100%);
    border-radius: 6px;
    opacity: 0.85;
  }
  .brand-name, .tagline {
    position: absolute; color: var(--brand-red);
    white-space: nowrap; line-height: 1; font-weight: 300;
  }
  .rule-h { position: absolute; height: 0; border-top: 1px dotted var(--brand-red); }
  .rule-v { position: absolute; width: 0; border-left: 1px dotted var(--brand-red); }

  /* card front */
  .card-front .mascot { left: 302px; top: 209px; width: 45px; height: 68px; }
  .card-front .brand-name { right: 24px; top: 243px; font-size: 40px; }
  .card-front .tagline { right: 15px; top: 282px; font-size: 23px; }
  .card-front .rule-h { left: 7px; right: 8px; top: 314px; }

  /* card back */
  .card-back .mascot { left: 402px; top: 11px; width: 33px; height: 51px; }
  .card-back .brand-name { right: 15px; top: 42px; font-size: 20px; }
  .card-back .tagline { right: 12px; top: 65px; font-size: 18px; }
  .card-back .rule-h { left: 109px; width: 339px; top: 160px; }

  .contact { position: absolute; left: 48px; top: 191px; font-size: 12.5px; color: var(--ink); font-weight: 400; }
  .contact-row { position: relative; height: 22px; }
  .contact-label { color: var(--brand-red); }
  .contact-cont { display: block; padding-left: 50px; line-height: 14px; }
  .contact-row.location { height: 36px; }

  .services { position: absolute; left: 361px; top: 172px; list-style: none;
    font-size: 12.5px; line-height: 14px; color: var(--ink); font-weight: 400; }
  .services li::before { content: "★"; color: var(--brand-red); font-size: 7px;
    display: inline-block; width: 12px; vertical-align: 2px; }

  /* letterhead */
  .letterhead .mascot { left: 343px; top: 13px; width: 42px; height: 67px; }
  .letterhead .brand-name { right: 18px; top: 48px; font-size: 39px; }
  .letterhead .tagline { right: 8px; top: 86px; font-size: 23px; }
  .letterhead .rule-h { left: 0; right: 0; top: 121px; }
  .letterhead .rule-v { left: 19px; top: 0; bottom: 0; }
</style>
</head>
<body>
<main class="canvas">

  <section class="sheet card-front" aria-label="Business card front">
    <div class="mascot" role="img" aria-label="Cartoon cleaner with mop and bucket"></div>
    <span class="brand-name">Tolvane</span>
    <span class="tagline">Lawnmowing and Property Maintenance</span>
    <div class="rule-h"></div>
  </section>

  <section class="sheet card-back" aria-label="Business card back">
    <div class="mascot" role="img" aria-label="Cartoon cleaner with mop and bucket"></div>
    <span class="brand-name">Tolvane</span>
    <span class="tagline">Lawnmowing and Property Maintenance</span>
    <div class="rule-h"></div>

    <div class="contact">
      <div class="contact-row"><span class="contact-label">Phone No.:</span> 0491726048, 0478301652</div>
      <div class="contact-row location">
        <span class="contact-label">Location:</span> 14 Barlowe Crescent
        <span class="contact-cont">Wexley Heights NSW 2184</span>
      </div>
      <div class="contact-row"><span class="contact-label">Abn number:</span> 64 907 518 243</div>
    </div>

    <ul class="services">
      <li>Garden Maintenance</li>
      <li>Mowing</li>
      <li>Trimming trees</li>
      <li>Blowing leaves</li>
      <li>Dusting</li>
      <li>Vacuuming</li>
      <li>Window cleaning</li>
    </ul>
  </section>

  <section class="sheet letterhead" aria-label="Letterhead">
    <div class="mascot" role="img" aria-label="Cartoon cleaner with mop and bucket"></div>
    <span class="brand-name">Tolvane</span>
    <span class="tagline">Lawnmowing and Property Maintenance</span>
    <div class="rule-h"></div>
    <div class="rule-v"></div>
  </section>

</main>
</body>
</html>
```